KT Crewing business card

Require business card which includes:
Company name: KT CREWING PTY LTD
Email: Mick@ktcrewing.com.au
Phone: 0431 556 208
ACN: 517 238 649

slogan: Onsite Auto Electrician Labour hire

Details and logo on top side
Logo only on bottom side

colour codes : #F15A29 , #939598

Target Market(s)

Western Australia mining sector

Industry/Entity Type

Mining

Contact Information for Business Card

Require business card which includes: Company name: KT CREWING PTY LTD Email: Mick@ktcrewing.com.au Phone: 0431 556 208 ACN: 517 238 649 slogan: Onsite Auto Electrician Labour hire Details and logo on top side Logo only on bottom side colour codes : #F15A29 , #939598

Colors
EE7325
F08F49
F5BC92
FAE3D3
FDF4ED

Requirements
Must have
• double sided

```html
<!DOCTYPE html>
<html lang="en">
<head>
<meta charset="utf-8">
<title>KT Crewing – Business Card</title>
<link href="https://fonts.googleapis.com/css2?family=Montserrat:wght@400;500;700&display=swap" rel="stylesheet">
<style>
  :root {
    --orange: #F15A29;
    --grey: #939598;
    --ink: #222222;
    --card: #FFFFFF;
    --backdrop: #D9D9DB;
  }
  html, body {
    margin: 0;
    padding: 0;
    width: 1200px;
    height: 962px;
    overflow: hidden;
    background: var(--backdrop);
    font-family: "Montserrat", sans-serif;
  }
  .sheet {
    position: relative;
    width: 1200px;
    height: 962px;
  }
  .card {
    position: absolute;
    left: 280px;
    width: 640px;
    height: 366px;
    background: var(--card);
    border-radius: 26px;
    box-shadow: 0 6px 18px rgba(0,0,0,0.12);
    overflow: hidden;
  }
  .card--back { top: 80px; }
  .card--front { top: 516px; }

  .brand {
    display: flex;
    align-items: center;
    gap: 14px;
  }
  .brand__mark {
    width: 34px;
    height: 34px;
    background: var(--orange);
  }
  .brand__name {
    font-weight: 700;
    color: var(--orange);
    letter-spacing: 1px;
    white-space: nowrap;
  }

  /* back side */
  .card--back .brand {
    position: absolute;
    left: 0; right: 0;
    top: 120px;
    justify-content: center;
  }
  .card--back .brand__name { font-size: 50px; }
  .card--back .brand__mark { width: 44px; height: 44px; }
  .slogan {
    position: absolute;
    left: 0; right: 0;
    top: 232px;
    text-align: center;
    font-size: 17px;
    font-weight: 500;
    color: var(--ink);
    letter-spacing: 0.3px;
  }

  /* front side */
  .card--front .brand {
    position: absolute;
    right: 52px;
    top: 48px;
  }
  .card--front .brand__name { font-size: 36px; }
  .divider {
    position: absolute;
    height: 1.5px;
    background: var(--ink);
  }
  .divider--top { left: 40px; right: 44px; top: 134px; }
  .divider--bottom { left: 40px; width: 240px; top: 252px; }
  .company {
    position: absolute;
    right: 48px;
    top: 150px;
    text-align: right;
    font-size: 15px;
    font-weight: 500;
    color: var(--ink);
    line-height: 1.5;
  }
  .person {
    position: absolute;
    left: 40px;
    top: 182px;
  }
  .person__name {
    font-size: 28px;
    font-weight: 700;
    color: var(--orange);
    margin: 0;
    letter-spacing: 0.5px;
  }
  .person__role {
    font-size: 17px;
    font-weight: 500;
    color: var(--ink);
    margin: 2px 0 0;
  }
  .contact {
    position: absolute;
    left: 40px;
    top: 264px;
    list-style: none;
    margin: 0;
    padding: 0;
    font-size: 17px;
    font-weight: 500;
    color: var(--ink);
  }
  .contact__item {
    display: flex;
    align-items: center;
    gap: 12px;
    height: 28px;
  }
  .contact__icon {
    width: 16px;
    height: 16px;
    flex: none;
  }
</style>
</head>
<body>
<main class="sheet">

  <section class="card card--back" aria-label="Card back">
    <div class="brand">
      <span class="brand__mark"></span>
      <span class="brand__name">KT Crewing</span>
    </div>
    <p class="slogan">Onsite Auto Electrician Labour hire</p>
  </section>

  <section class="card card--front" aria-label="Card front">
    <div class="brand">
      <span class="brand__mark"></span>
      <span class="brand__name">KT Crewing</span>
    </div>
    <div class="divider divider--top"></div>
    <div class="company">
      KT CREWING PTY LTD<br>
      ACN: 517 238 649
    </div>

    <div class="person">
      <h1 class="person__name">LIAM CARTER</h1>
      <p class="person__role">Managing Director</p>
    </div>
    <div class="divider divider--bottom"></div>

    <ul class="contact">
      <li class="contact__item">
        <svg class="contact__icon" viewBox="0 0 16 16" aria-hidden="true">
          <path d="M3.5 1.5l2.5 3-1.5 1.5c.8 1.8 2.2 3.2 4 4l1.5-1.5 3 2.5-1.5 2.5C7 13.5 2.5 9 1 3z" fill="var(--orange)"/>
        </svg>
        0431 556 208
      </li>
      <li class="contact__item">
        <svg class="contact__icon" viewBox="0 0 16 16" aria-hidden="true">
          <rect x="1" y="3" width="14" height="10" fill="var(--orange)"/>
          <path d="M1 3l7 6 7-6" fill="none" stroke="#fff" stroke-width="1.2"/>
        </svg>
        Mick@ktcrewing.com.au
      </li>
      <li class="contact__item">
        <svg class="contact__icon" viewBox="0 0 16 16" aria-hidden="true">
          <circle cx="8" cy="8" r="7" fill="var(--orange)"/>
          <ellipse cx="8" cy="8" rx="3" ry="7" fill="none" stroke="#fff" stroke-width="1"/>
          <path d="M1 8h14" stroke="#fff" stroke-width="1"/>
        </svg>
        Your webadress here
      </li>
    </ul>
  </section>

</main>
</body>
</html>
```